Facebook Advert for caravan storage & Caravan sales products

We are Pellowdene Leisure.

History about us!!
Pellowdene store close to 300 touring caravans in Cornwall UK, We also sell caravans by buying & selling ourselves or via our brokerage service. Pellowdene also has a small Caravan park.

What i want
I would like a Bold advert designed that can be placed on my facebook page & also on a series of Facebook selling groups. I would like my logo on it also the cartoon picture of me.

Make sure you point out we are based in Cornwall, I would like the following somewhere on the advert.

The brokerage advantages: can help arrange finance, we can take px back against your caravan, Let us sell your caravan, List of waiting buyers, Free storage while its up for sale. (do not just copy this please shorten it for an advert, mix it up if you have to)

Please also try put somewhere "We buy caravans" transport available
& secure storage available, 01347 62814 www.pellowdeneleisure.example.co.uk

Target Market(s)

People looking to sell or buy touring caravans

Colors

Designer to choose colors to be used in the design.

Requirements
Must have
• Colour
• Boldness
• Bright
• To the point

```html
<!DOCTYPE html>
<html lang="en">
<head>
<meta charset="utf-8">
<title>Pellowdene Leisure – Caravan Sales &amp; Storage, Cornwall</title>
<link rel="stylesheet" href="https://fonts.googleapis.com/css2?family=Montserrat:wght@400;500;600;700&family=Roboto+Condensed:wght@300;400&family=Roboto:wght@400&display=swap">
<style>
  :root {
    --brand-blue: #2a82d0;
    --band-cyan: #3ba6da;
    --bubble-light: #cfeaf8;
    --bubble-mid: #8fcbeb;
    --bubble-deep: #6fb6e0;
    --white: #ffffff;
    --page: #ffffff;
  }
  * { margin: 0; padding: 0; box-sizing: border-box; }
  html, body {
    width: 1009px; height: 1200px; overflow: hidden; background: var(--page);
  }
  .hanger {
    position: relative; width: 1009px; height: 1200px; color: var(--white);
  }
  .hanger-shape { position: absolute; inset: 0; }
  .owner-portrait {
    position: absolute; left: 555px; top: 688px; width: 426px; height: 418px;
    border-radius: 50%;
    background: radial-gradient(circle at 40% 30%, var(--bubble-light), var(--bubble-mid) 70%, var(--bubble-deep));
  }
  .brand-name {
    position: absolute; left: 56px; top: 714px; width: 430px; text-align: center;
    font: 600 43px/1 "Montserrat", sans-serif; letter-spacing: -0.5px;
  }
  .brand-tagline {
    position: absolute; left: 56px; top: 768px; width: 430px; text-align: center;
    font: 500 22px/1 "Montserrat", sans-serif; white-space: nowrap;
  }
  .rule {
    position: absolute; left: 56px; width: 504px; height: 1px; background: var(--white);
  }
  .rule--top { top: 822px; }
  .rule--bottom { top: 925px; }
  .brokerage-note {
    position: absolute; left: 64px; top: 830px; width: 490px;
    font: 300 23px/1.32 "Roboto Condensed", sans-serif;
  }
  .brokerage-note span { display: block; white-space: nowrap; }
  .headline {
    position: absolute; left: 58px; top: 946px;
    font: 700 44px/1 "Montserrat", sans-serif; letter-spacing: 1px; white-space: nowrap;
  }
  .subhead {
    position: absolute; left: 60px; top: 1004px;
    font: 400 35px/1 "Montserrat", sans-serif; letter-spacing: 1.5px; white-space: nowrap;
  }
  .web-band {
    position: absolute; left: 31px; top: 1060px; width: 572px; height: 45px;
    background: var(--band-cyan); display: flex; align-items: center; padding-left: 30px; gap: 22px;
  }
  .web-band svg { width: 28px; height: 28px; flex: none; }
  .web-address { font: 400 25px/1 "Roboto", sans-serif; letter-spacing: 0.5px; white-space: nowrap; }
  .phone {
    position: absolute; left: 112px; top: 1128px;
    font: 400 31px/1 "Roboto Condensed", sans-serif; letter-spacing: 1px;
  }
</style>
</head>
<body>
<div class="hanger">
  <svg class="hanger-shape" width="1009" height="1200" viewBox="0 0 900 1090" preserveAspectRatio="none" aria-hidden="true">
    <path fill="var(--brand-blue)" d="M138 460 L138 300 C138 130 280 10 440 10 C580 10 690 90 740 205 L580 205 C545 170 495 150 440 150 C340 150 275 220 275 310 L275 460 Z"/>
    <rect x="18" y="435" width="864" height="640" rx="50" fill="var(--brand-blue)"/>
  </svg>

  <div class="owner-portrait" role="img" aria-label="Cartoon portrait of the owner in a blue branded t-shirt giving a thumbs up"></div>

  <div class="brand-name">Pellowdene Leisure</div>
  <div class="brand-tagline">— Cornwall caravan sales &amp; storage —</div>

  <div class="rule rule--top"></div>
  <p class="brokerage-note">
    <span>Let us sell your caravan, List of waiting buyers,</span>
    <span>Free storage while it's up for sale, PX welcome,</span>
    <span>Finance arranged, Secure storage available.</span>
  </p>
  <div class="rule rule--bottom"></div>

  <h1 class="headline">WE BUY CARAVANS</h1>
  <p class="subhead">TRANSPORT AVAILABLE</p>

  <div class="web-band">
    <svg viewBox="0 0 24 24" aria-hidden="true">
      <circle cx="12" cy="12" r="10" fill="none" stroke="#fff" stroke-width="2"/>
      <ellipse cx="12" cy="12" rx="4.5" ry="10" fill="none" stroke="#fff" stroke-width="1.6"/>
      <path d="M2 12h20M4 7h16M4 17h16" stroke="#fff" stroke-width="1.6"/>
    </svg>
    <span class="web-address">www.pellowdeneleisure.example.co.uk</span>
  </div>

  <p class="phone">Call Us : 01347 62814</p>
</div>
</body>
</html>
```